Flyer-Design für Werbeflyer Teamentwicklung/Coaching als pdf
Zielgruppe
ich berate Personen, Teams und Organisationseinheiten, überwiegend im Profitbereich. (Internationale Konzerne). Mein Beratungsspektrum ist Führung, Prozessverbesserungen, Teamentwicklung
Aufgabenstellung
Der Text ist in Anlehnung an meine HP, Teamentwicklung und Coaching und es sollte eine übersichtliche, infomative 1-2 Seiten entstehen, die ich als erste Werbung/Kontaktaufnahme versenden kann. Die Seiten sollen klar einen Überblick über mein "Schaffen" geben, sollen aber auch schon etwas von meiner Arbeitsweise deutlich machen. (Ich begriefe schnell, formuliere klar und arbeite sehr zielorientiert - allerdings auch schnörkellos!) Diese Seiten sollten überwiegend als Anhang an eine Mail fungieren, im Ausnahmefall aber auch versendet werden.
Das Logo, die Farbe, etc. analog zu meiner HP - ich lass mich da aber auch gern beraten, falls sie andere Ideen haben

```html
<!DOCTYPE html>
<html lang="de">
<head>
<meta charset="utf-8">
<title>Teamentwicklung Brigitte Morawe</title>
<link href="https://fonts.googleapis.com/css2?family=Open+Sans:wght@400;600&display=swap" rel="stylesheet">
<style>
  :root {
    --sage: #b9c9c4;
    --slate: #6b7673;
    --plum: #760050;
    --white: #ffffff;
    --sky-top: #3b8fd8;
    --sky-mid: #c9dcea;
    --deck: #6f6a63;
  }
  * { margin: 0; padding: 0; box-sizing: border-box; }
  html, body { width: 1120px; height: 1200px; overflow: hidden; background: var(--white); }
  body { position: relative; font-family: "Open Sans", Arial, sans-serif; color: var(--slate); }

  .top-band { position: absolute; left: 0; top: 60px; width: 1120px; height: 114px; background: var(--sage); }
  .brand-mark {
    position: absolute; left: 596px; top: 60px; width: 121px; height: 114px;
    background: var(--white); display: flex; flex-direction: column;
    align-items: center; justify-content: center; gap: 8px;
  }
  .brand-mark .square { width: 26px; height: 26px; background: var(--slate); }
  .brand-mark .name { font-size: 17px; font-weight: 600; color: var(--slate); letter-spacing: 1px; }
  .accent-bar { position: absolute; left: 939px; top: 0; width: 108px; height: 260px; background: var(--plum); }

  .headline { position: absolute; right: 73px; top: 332px; text-align: right; font-weight: 600; text-transform: uppercase; }
  .headline .title { font-size: 46px; line-height: 48px; letter-spacing: 0.5px; color: var(--slate); }
  .headline .owner { font-size: 34px; line-height: 40px; color: var(--slate); }
  .headline .owner span { color: var(--plum); }

  .hero-photo {
    position: absolute; left: 0; top: 443px; width: 1120px; height: 512px;
    background: linear-gradient(180deg, var(--sky-top) 0%, var(--sky-mid) 45%, #9fb9c4 62%, #8b8780 72%, var(--deck) 100%);
  }

  .contact-panel {
    position: absolute; left: 0; top: 505px; width: 348px; height: 353px;
    background: rgba(255,255,255,0.78); padding: 20px 0 0 53px;
  }
  .contact-panel h2 { font-size: 40px; font-weight: 400; line-height: 46px; letter-spacing: 1px; color: var(--slate); }
  .contact-panel .person { font-size: 20px; color: var(--plum); margin-top: 8px; line-height: 26px; }
  .contact-panel address, .contact-panel .lines { font-style: normal; font-size: 21px; line-height: 25.5px; color: var(--slate); }
  .contact-panel address { margin-top: 20px; }
  .contact-panel .lines { margin-top: 24px; }

  .bottom-band { position: absolute; left: 0; top: 1077px; width: 1120px; height: 44px; background: var(--sage); }
</style>
</head>
<body>
  <div class="top-band"></div>
  <div class="brand-mark"><div class="square"></div><div class="name">Morawe</div></div>
  <div class="accent-bar"></div>

  <header class="headline">
    <div class="title">Teamentwicklung</div>
    <div class="owner">Brigitte <span>Morawe</span></div>
  </header>

  <div class="hero-photo" role="img" aria-label="Fotografie eines hölzernen Seestegs mit Geländer, der unter blauem Himmel mit Wolken aufs Meer hinausführt"></div>

  <section class="contact-panel">
    <h2>KONTAKT</h2>
    <p class="person">Brigitte Morawe</p>
    <address>Ahorncenter<br>Ahornweg 12-14<br>90431 Musterstadt</address>
    <p class="lines">Tel:&nbsp; 0911 - 12 34 56<br>Fax: 0911 - 6 54 32 10<br>info@brigitte-morawe.de<br>www.brigitte-morawe.de</p>
  </section>

  <div class="bottom-band"></div>
</body>
</html>
```